Faithful Harbor Fellowship Network needs a fresh new web design

We are an up and coming multicultural church that aims to bring people into a life changing encounter with God. We need a fresh and inviting website in order to increase our internet presence and make us easier to connect with.
Here are some of the basic requirements for the site:
• Clearly displayed address, service times, and contact info
• A staff profile page
• An area for a calendar with upcoming events and their details
• Social media buttons
• Group pages for the different ministries (youth, children’s church, men, etc…)
• An area for donations and eCommerce
• A resources page for assorted media (podcasts, sermons, videos, etc.…)
• An area for prayer requests.

Industry/Entity Type

Church

```html
<!DOCTYPE html>
<html lang="en">
<head>
<meta charset="utf-8">
<title>Faithful Harbor Fellowship Network</title>
<link rel="stylesheet" href="https://fonts.googleapis.com/css2?family=Open+Sans:ital,wght@0,400;0,600;0,700;1,400;1,600&family=Source+Sans+3:wght@400;600&display=swap">
<style>
:root{
  --navy:#1f2a5c;
  --ink:#333;
  --muted:#777;
  --line:#d8d8d8;
  --brown:#7a4f35;
  --brown-dark:#5e3a25;
  --yellow:#f2c500;
  --band:#ececec;
  --footer:#050505;
  --footer-text:#8d96b8;
  --white:#fff;
}
*{margin:0;padding:0;box-sizing:border-box}
html,body{width:1200px;height:1112px;overflow:hidden;background:var(--white)}
body{position:relative;font-family:"Open Sans",Arial,sans-serif;color:var(--ink)}
.abs{position:absolute}

.brand{left:290px;top:36px;display:flex;align-items:center;gap:10px}
.brand-dot{width:34px;height:34px;border-radius:50%;background:var(--navy)}
.brand-name{font-size:15px;font-weight:700;color:var(--navy);line-height:17px;width:150px}

.main-nav{left:590px;top:46px;display:flex;font-size:8.5px;color:#444;letter-spacing:.2px}
.main-nav span{padding:0 10px;border-left:1px solid #bbb;line-height:10px}
.main-nav span:first-child{border:0;padding-left:4px;padding-right:20px;color:var(--navy)}
.nav-rule{left:290px;top:75px;width:655px;height:1px;background:var(--line)}
.nav-active{left:593px;top:73px;width:24px;height:5px;background:var(--yellow)}

.sermon-meta{left:290px;width:655px;top:101px;text-align:center;font-size:7.5px;font-style:italic;color:#555}
.sermon-quote{left:410px;width:415px;top:114px;text-align:center;font-family:"Source Sans 3",sans-serif;font-size:14px;line-height:17px;color:var(--navy)}

.hero{left:290px;top:160px;width:655px;height:268px;background:radial-gradient(ellipse at 80% 20%,#eef4fb 0%,#7a9bbd 18%,#4b4a5a 40%,#1a1a22 70%,#0a0a0a 100%)}
.hero-caption{left:290px;top:376px;width:655px;height:43px;background:rgba(90,90,90,.75);color:#eee;font-size:10px;letter-spacing:.3px;text-align:center;line-height:43px}
.arrow{width:38px;height:38px}

.feature-band{left:0;top:428px;width:1200px;height:197px;background:linear-gradient(#e3e3e3,#fff)}
.feature-panel{left:290px;top:428px;width:655px;height:196px;background:var(--brown)}
.feature{position:absolute;top:40px;width:156px;color:var(--white)}
.feature-photo{width:156px;height:86px;border:4px solid var(--white);position:relative}
.read-more{position:absolute;left:4px;bottom:8px;background:var(--brown-dark);font-size:7px;padding:4px 8px;color:#f3e7dc}
.feature h3{font-size:9px;font-weight:400;margin-top:12px;letter-spacing:.3px}
.feature p{font-size:7px;line-height:10px;margin-top:6px;color:#f1e4da}

.col-title{font-size:9px;color:var(--navy);letter-spacing:.2px}
.news-item{left:290px;width:200px;height:64px}
.news-photo{position:absolute;left:0;top:0;width:88px;height:62px;border:1px solid #ddd;padding:3px}
.news-photo div{width:100%;height:100%;background:linear-gradient(#f1ebe4,#d7b9a4 60%,#c65a5a)}
.news-item h4{position:absolute;left:98px;top:0;font-size:8.5px;font-weight:400;color:#444}
.news-item p{position:absolute;left:98px;top:16px;width:104px;font-size:6.5px;line-height:9px;color:var(--muted)}
.news-item small{position:absolute;left:100px;top:54px;font-size:5.5px;color:#555}
.news-sep{left:378px;width:114px;height:1px;background:var(--line)}

.event{left:537px;width:140px;height:50px}
.event-date{position:absolute;left:0;top:0;width:24px;text-align:center}
.event-date b{display:block;background:#eee;font-size:13px;font-weight:400;color:#999;height:22px;line-height:22px}
.event-date span{display:block;font-size:7px;color:#aaa;margin-top:4px}
.event h4{position:absolute;left:39px;top:2px;font-size:8.5px;font-weight:400;color:#555;white-space:nowrap}
.event p{position:absolute;left:39px;top:16px;font-size:6px;line-height:13px;color:#777}
.event-sep{left:563px;width:114px;height:1px;background:var(--line)}

.join-text{left:742px;top:669px;width:205px;font-size:6.5px;line-height:9.5px;color:#555}
.join-quote{left:742px;top:718px;width:205px;font-family:"Source Sans 3",sans-serif;font-size:9.5px;line-height:12px;color:var(--navy)}
.join-author{left:742px;top:764px;font-size:8.5px;font-style:italic;font-weight:600;color:var(--navy)}
.service-title{left:788px;top:794px;font-size:8.5px;color:var(--navy)}
.service-times{left:788px;top:807px;width:157px;height:16px;background:#e9e9e9;border:1px solid #ccc;font-size:7px;color:#555;line-height:14px;padding-left:8px}

.members-band{left:290px;top:840px;width:655px;height:125px;background:#f1f1f1}
.members-rule{left:349px;top:864px;width:526px;height:1px;background:#c8c8c8}
.members-title{left:570px;top:856px;width:82px;background:#f1f1f1;text-align:center;font-size:9px;color:var(--navy)}
.members-dot{width:6px;height:6px;border-radius:50%;background:#bbb;top:861px}
.member{top:883px;width:127px}
.member-photo{height:80px;border:1px solid #ccc;background:var(--white);padding:4px}
.member-photo div{width:100%;height:100%}
.member-name{margin-top:5px;height:17px;background:#c7c7c7;font-size:8.5px;color:#333;line-height:17px;padding-left:22px}

.site-footer{left:0;top:1004px;width:1200px;height:108px;background:var(--footer)}
.footer-brand{left:290px;top:1030px;display:flex;align-items:center;gap:6px}
.footer-brand i{width:24px;height:24px;border-radius:50%;background:#777}
.footer-brand span{font-size:9px;font-weight:700;color:#999;line-height:11px;width:88px}
.footer-title{font-size:8.5px;color:#ddd;letter-spacing:.3px}
.contact-line{left:464px;display:flex;gap:8px;font-size:7px;line-height:10px;color:var(--footer-text)}
.contact-line svg{flex:none}
.social{left:656px;top:1044px;display:flex;gap:5px}
.social i{width:14px;height:14px;background:#555}
.legal{left:790px;top:1043px;width:155px;text-align:right;font-size:5.5px;line-height:10px;color:#888}
</style>
</head>
<body>

<header>
  <div class="abs brand"><span class="brand-dot"></span><span class="brand-name">Faithful Harbor Fellowship Network</span></div>
  <nav class="abs main-nav"><span>HOME</span><span>CALENDER</span><span>MINISTERIES</span><span>SERVICE TIMING</span><span>SERMONS</span><span>CONTACT US</span></nav>
  <div class="abs nav-rule"></div>
  <div class="abs nav-active"></div>
</header>

<p class="abs sermon-meta">Latest Sermon: &nbsp;The Open Invitation - &nbsp;04 May 2014</p>
<p class="abs sermon-quote">Blessed is the man that endureth temptation for when he is tried he shall receive the crown of life.</p>

<section>
  <div class="abs hero" role="img" aria-label="White dove in flight against a dark sky with rays of sunlight breaking through clouds"></div>
  <p class="abs hero-caption">DOUBTS ARE THE ANTS IN THE PANTS OF FAITH. THEY KEEP IT AWAKE AND MOVING.</p>
  <svg class="abs arrow" style="left:231px;top:273px" viewBox="0 0 38 38"><circle cx="19" cy="19" r="18" fill="none" stroke="#aaa" stroke-width="1.2"/><path d="M22 12l-7 7 7 7" fill="none" stroke="#999" stroke-width="1.5"/></svg>
  <svg class="abs arrow" style="left:964px;top:276px" viewBox="0 0 38 38"><circle cx="19" cy="19" r="18" fill="none" stroke="var(--navy)" stroke-width="1.4"/><path d="M16 12l7 7-7 7" fill="none" stroke="var(--navy)" stroke-width="1.8"/></svg>
</section>

<section>
  <div class="abs feature-band"></div>
  <div class="abs feature-panel">
    <div class="feature" style="left:51px">
      <div class="feature-photo" role="img" aria-label="Wooden jetty reaching into a calm lake at sunset" style="background:linear-gradient(#c9a07a,#e8c79b 45%,#5f8c8a)"><span class="read-more">read more</span></div>
      <h3>ABOUT US</h3><p>Lorem Ipsum is simply dummy text of the printing and typesetting industry.</p>
    </div>
    <div class="feature" style="left:246px">
      <div class="feature-photo" role="img" aria-label="Black and white cathedral towers with sunlight" style="background:linear-gradient(#8a8a8a,#e0e0e0 50%,#555)"><span class="read-more">read more</span></div>
      <h3>SERMONS</h3><p>Lorem Ipsum is simply dummy text of the printing and typesetting industry.</p>
    </div>
    <div class="feature" style="left:446px">
      <div class="feature-photo" role="img" aria-label="Hands holding a small wooden cross on a cord" style="background:linear-gradient(135deg,#d9a693,#a8695a 55%,#e2b8a8)"><span class="read-more">read more</span></div>
      <h3>MINISTRIES</h3><p>Lorem Ipsum is simply dummy text of the printing and typesetting industry.</p>
    </div>
  </div>
</section>

<section>
  <h2 class="abs col-title" style="left:290px;top:646px">LATEST NEWS</h2>
  <article class="abs news-item" style="top:674px">
    <div class="news-photo"><div role="img" aria-label="Young child in a striped top"></div></div>
    <h4>News Heading Here</h4>
    <p>Lorem ipsum dolor sit amet, con-sectetur adipiscing elit. Nulla iaculis aliquet augue, eu varius.</p>
    <small>read more</small>
  </article>
  <div class="abs news-sep" style="top:745px"></div>
  <article class="abs news-item" style="top:753px">
    <div class="news-photo"><div role="img" aria-label="Young child in a striped top"></div></div>
    <h4>News Heading Here</h4>
    <p>Lorem ipsum dolor sit amet, con-sectetur adipiscing elit. Nulla iaculis aliquet</p>
    <small>read more</small>
  </article>

  <h2 class="abs col-title" style="left:537px;top:646px">UPCOMING EVENTS</h2>
  <div class="abs event" style="top:674px"><div class="event-date"><b>04</b><span>MAY</span></div><h4>Upcoming Heading Here</h4><p>Harbor Hall, Bird Way<br>10.20</p></div>
  <div class="abs event-sep" style="top:721px"></div>
  <div class="abs event" style="top:731px"><div class="event-date"><b>12</b><span>MAY</span></div><h4>Upcoming Heading Here</h4><p>Harbor Hall, Bird Way<br>10.20</p></div>
  <div class="abs event-sep" style="top:776px"></div>
  <div class="abs event" style="top:786px"><div class="event-date"><b>18</b><span>MAY</span></div><h4>Upcoming Heading Here</h4><p>Harbor Hall, Bird Way<br>10.20</p></div>

  <h2 class="abs col-title" style="left:742px;top:646px">JOIN OUR COMMUNITY</h2>
  <p class="abs join-text">Lorem Ipsum is simply dummy text of the printing and typesetting industry. Lorem Ipsum has been the industry's standard dummy text ever since the 1500s</p>
  <p class="abs join-quote">“ Blessed is the man that endureth temptation for when he is tried he shall receive the crown of life. ”</p>
  <p class="abs join-author">- Elias Marlow</p>
  <svg class="abs" style="left:740px;top:794px" width="32" height="32" viewBox="0 0 32 32"><circle cx="16" cy="16" r="15" fill="none" stroke="#999" stroke-width="1.5"/><path d="M16 7v9l-4 4" fill="none" stroke="#999" stroke-width="1.5"/></svg>
  <p class="abs service-title">CHURCH SERVICES</p>
  <p class="abs service-times">Sunday 10 am. &nbsp;| &nbsp;3.00 pm. &nbsp;| &nbsp;6.00 pm.</p>
</section>

<section>
  <div class="abs members-band"></div>
  <div class="abs members-rule"></div>
  <span class="abs members-dot" style="left:566px"></span>
  <span class="abs members-dot" style="left:650px"></span>
  <h2 class="abs members-title">OUR MEMBERS</h2>
  <div class="abs member" style="left:349px"><div class="member-photo"><div role="img" aria-label="Portrait of a team member" style="background:linear-gradient(#3f7fc0,#6fa4d8)"></div></div><p class="member-name">Mara Ellison</p></div>
  <div class="abs member" style="left:482px"><div class="member-photo"><div role="img" aria-label="Portrait of a team member" style="background:linear-gradient(#f4f4f4,#d9b3a0)"></div></div><p class="member-name">Nadia Hollis</p></div>
  <div class="abs member" style="left:615px"><div class="member-photo"><div role="img" aria-label="Portrait of a team member" style="background:linear-gradient(#5cc6d8,#e0b9a0)"></div></div><p class="member-name">Owen T</p></div>
  <div class="abs member" style="left:748px"><div class="member-photo"><div role="img" aria-label="Portrait of a team member" style="background:linear-gradient(#c9ccd3,#e7cda6)"></div></div><p class="member-name">June Farrow</p></div>
</section>

<footer class="abs site-footer">
  <div class="abs footer-brand" style="left:290px;top:22px"><i></i><span>Faithful Harbor Fellowship Network</span></div>
  <h3 class="abs footer-title" style="left:464px;top:27px">VISIT US</h3>
  <p class="abs contact-line" style="top:43px"><svg width="9" height="9" viewBox="0 0 10 10"><circle cx="5" cy="4" r="3" fill="none" stroke="#aaa"/><path d="M5 7v3" stroke="#aaa"/></svg><span>48 Willow Bend Lane in Brookhaven,<br>NY, USA.</span></p>
  <p class="abs contact-line" style="top:70px"><svg width="9" height="9" viewBox="0 0 10 10"><rect x="1" y="2" width="8" height="6" rx="1" fill="#aaa"/></svg><span>+00 123 456 7890</span></p>
  <p class="abs contact-line" style="top:86px"><svg width="9" height="9" viewBox="0 0 10 10"><rect x=".5" y="2" width="9" height="6" fill="none" stroke="#aaa"/><path d="M.5 2l4.5 3 4.5-3" fill="none" stroke="#aaa"/></svg><span>info@faithfulharbor.org</span></p>
  <h3 class="abs footer-title" style="left:656px;top:27px">FOLLOW US</h3>
  <div class="abs social" style="top:40px"><i></i><i></i><i></i><i></i></div>
  <p class="abs legal" style="top:39px">Copyright © 2014. Company Name. All rights reserved<br>Privacy Policy</p>
</footer>

</body>
</html>
```